Very high end short term vacation rentals.

Amber Tide Harbor Estates. Design business cards using existing logo. Should represent high quality, class accommodations. The back side will have a QR code linking to website/video and pictures

```html
<!DOCTYPE html>
<html lang="en">
<head>
<meta charset="utf-8">
<title>Amber Tide Harbor Estates – Business Cards</title>
<link href="https://fonts.googleapis.com/css2?family=Cinzel:wght@500&family=Poppins:wght@400&display=swap" rel="stylesheet">
<style>
  :root {
    --canvas: #e8e8e8;
    --card-white: #fbfbfb;
    --ink: #0b0b0b;
    --ink-soft: #3a3a3a;
    --rule: #9a9a9a;
    --band-grey: #6f6f6f;
    --white: #f4f4f4;
  }
  * { margin: 0; padding: 0; box-sizing: border-box; }
  html, body { width: 1200px; height: 1085px; overflow: hidden; background: var(--canvas); }
  .sheet { position: relative; width: 1200px; height: 1085px; }

  .card {
    position: absolute; left: 301px; width: 579px; height: 343px;
    box-shadow: 2px 2px 3px rgba(0,0,0,.35);
    overflow: hidden;
  }
  .card--front { top: 164px; background: var(--card-white); }
  .card--back  { top: 543px; background: var(--ink); }

  .brand-ring { position: absolute; border-radius: 50%; }
  .card--front .brand-ring { left: 81px; top: 66px; width: 136px; height: 136px; border: 3px solid var(--ink); }
  .card--back  .brand-ring { left: 78px; top: 115px; width: 110px; height: 110px; border: 3px solid var(--white); }

  .brand-name { position: absolute; font-family: "Cinzel", serif; font-weight: 500; letter-spacing: .5px; }
  .card--front .brand-name { left: 0; width: 302px; top: 204px; text-align: center; color: var(--ink); line-height: 1.15; }
  .card--front .brand-name .line-1 { display: block; font-size: 24px; }
  .card--front .brand-name .line-2 { display: block; font-size: 17px; }
  .card--back .brand-name { left: 228px; top: 134px; color: var(--white); line-height: 1.2; }
  .card--back .brand-name .line-1 { display: block; font-size: 32px; }
  .card--back .brand-name .line-2 { display: block; font-size: 23px; }

  .divider { position: absolute; width: 1px; background: var(--rule); }
  .card--front .divider { left: 283px; top: 61px; height: 208px; }
  .card--back  .divider { left: 210px; top: 118px; height: 84px; background: #bdbdbd; }

  .contact { position: absolute; left: 307px; top: 76px; font-family: "Poppins", sans-serif; color: var(--ink-soft); }
  .contact__name { font-family: "Cinzel", serif; font-weight: 500; font-size: 25px; color: var(--ink); line-height: 1; }
  .contact__title { font-size: 16px; margin-top: 6px; letter-spacing: .3px; }
  .contact__list { list-style: none; margin-top: 14px; font-size: 16px; line-height: 17.5px; }
  .contact__list li { display: flex; align-items: center; gap: 4px; }
  .contact__list svg { width: 13px; height: 13px; flex: none; }
  .contact__address { display: flex; gap: 5px; margin-top: 16px; font-size: 16px; line-height: 17.5px; }
  .contact__address svg { width: 12px; height: 15px; flex: none; margin-top: 1px; }

  .front-band { position: absolute; left: 0; bottom: 0; width: 579px; height: 40px; }
</style>
</head>
<body>
<main class="sheet">

  <section class="card card--front" aria-label="Front of business card">
    <div class="brand-ring"></div>
    <h1 class="brand-name"><span class="line-1">Amber Tide</span><span class="line-2">Harbor Estates</span></h1>
    <div class="divider"></div>

    <div class="contact">
      <p class="contact__name">Marlow Bennett</p>
      <p class="contact__title">Managing&nbsp; Director</p>
      <ul class="contact__list">
        <li><svg viewBox="0 0 24 24"><path fill="#0b0b0b" d="M6.6 10.8a15.5 15.5 0 0 0 6.6 6.6l2.2-2.2c.3-.3.7-.4 1-.2 1.1.4 2.3.6 3.6.6.6 0 1 .4 1 1V20c0 .6-.4 1-1 1C10.6 21 3 13.4 3 4c0-.6.4-1 1-1h3.5c.6 0 1 .4 1 1 0 1.3.2 2.5.6 3.6.1.3 0 .7-.2 1z"/></svg>044-123 456 789</li>
        <li><svg viewBox="0 0 24 24"><path fill="#0b0b0b" d="M2 5h20v14H2z M2 5l10 8 10-8" stroke="#fbfbfb" stroke-width="1.5"/></svg>info@email.com</li>
        <li><svg viewBox="0 0 24 24" fill="none" stroke="#0b0b0b" stroke-width="2"><circle cx="12" cy="12" r="10"/><path d="M2 12h20M12 2c3 3 3 17 0 20M12 2c-3 3-3 17 0 20"/></svg>www.website.com</li>
      </ul>
      <div class="contact__address">
        <svg viewBox="0 0 16 22"><path fill="#0b0b0b" d="M8 0a8 8 0 0 0-8 8c0 6 8 14 8 14s8-8 8-14a8 8 0 0 0-8-8zm0 11a3 3 0 1 1 0-6 3 3 0 0 1 0 6z"/></svg>
        <p>123, 7th street<br>Country name, 123456</p>
      </div>
    </div>

    <svg class="front-band" viewBox="0 0 579 40" aria-hidden="true">
      <polygon points="289,0 579,0 579,40 0,40 0,20 275,20" fill="#0b0b0b"/>
      <polygon points="0,8 277,8 272,15 0,15" fill="#6f6f6f"/>
    </svg>
  </section>

  <section class="card card--back" aria-label="Back of business card">
    <div class="brand-ring"></div>
    <div class="divider"></div>
    <h2 class="brand-name"><span class="line-1">Amber Tide</span><span class="line-2">Harbor Estates</span></h2>
  </section>

</main>
</body>
</html>
```